Global Expert Network Firm needs business card design

We need business card design for a new company based in Seoul, South Korea called 'Corwell Insight Partners'. We recruit industry experts covering all countries and connect our client and recruited expert by phone, face-to-face meetings and etc. We are a global expert network firm that is focused on delivering high-quality experts to our clients throughout the world. Our clients include multinational corporations, global consulting firms, private equity firms, venture capital firms, asset management companies.
We have made new logo and please find attachment.(Please use new logo)
Target Market(s)
Global Consulting Firms, Investment Firms, Private Equity Firms, Venture Capital Firms.
Industry/Entity Type
Recruitment
Contact Information for Business Card
We need two Languages (English and Korean Version).
The front is Korean and the back is English version.
[The back] [English]
Company Name: Corwell Insight Partners, Inc.
CEO Name: Daniel Park
Address: #507, Hanbit Bldg, 82 Maebongsan-ro, Dobong-gu, Seoul, 01327, Korea
Tel. +82 2 718 4052
Fax. +82 2 864 1097
Mobile. +82 10 7264 8815
Email: daniel@corwellip.com
Web: www.corwellip.com
[The front] [Korean] => Described in same order as English version.
회사명: 코웰인사이트파트너스(주)
대표이사: 박도현
주소: 서울시 도봉구 매봉산로 82 한빛빌딩 507호
Tel. 02 718 4052
Fax. 02 864 1097
Mobile. 010 7264 8815
Web: www.corwellip.com
Look and feel
Each slider illustrates characteristics of the customer's brand and the style your logo design should communicate.

```html
<!DOCTYPE html>
<html lang="en">
<head>
<meta charset="utf-8">
<title>Corwell Insight Partners – Business Card</title>
<link rel="stylesheet" href="https://fonts.googleapis.com/css2?family=Lato:wght@400;700;900&family=Exo+2:wght@300&family=Nunito:wght@400&family=Noto+Sans+KR:wght@300;400&display=swap">
<style>
  :root {
    --bg: #e6e8ec;
    --black: #000000;
    --navy: #1b2251;
    --white: #ffffff;
    --ink: #111111;
    --blue-name: #2a5cae;
    --muted: #b9bdcc;
  }
  html, body {
    margin: 0;
    padding: 0;
    width: 1200px;
    height: 1200px;
    overflow: hidden;
    background: var(--bg);
  }
  .canvas {
    position: relative;
    width: 1200px;
    height: 1200px;
  }
  .card {
    position: absolute;
    left: 191px;
    width: 818px;
    height: 491px;
    overflow: hidden;
    font-family: "Lato", sans-serif;
  }
  .card--english { top: 44px; }
  .card--korean { top: 635px; }

  .band { position: absolute; left: 0; width: 100%; }
  .band--black { top: 0; height: 292px; background: var(--black); }
  .band--white { top: 292px; height: 53px; background: var(--white); }
  .band--navy { top: 345px; height: 146px; background: var(--navy); }
  .card--korean .band--black { height: 294px; }
  .card--korean .band--white { top: 294px; height: 52px; }
  .card--korean .band--navy { top: 346px; height: 145px; }

  .brand {
    position: absolute;
    left: 56px;
    top: 62px;
    display: flex;
    align-items: flex-start;
    gap: 16px;
  }
  .brand__square {
    width: 44px;
    height: 44px;
    background: var(--navy);
    flex: none;
  }
  .brand__name {
    font-family: "Lato", sans-serif;
    font-weight: 400;
    font-size: 25px;
    line-height: 37px;
    color: var(--white);
    letter-spacing: 0.5px;
    margin-top: -4px;
  }

  .company-title {
    position: absolute;
    left: 499px;
    top: 48px;
    color: var(--white);
  }
  .company-title__main {
    font-weight: 900;
    font-size: 38px;
    line-height: 40px;
    letter-spacing: 0.5px;
  }
  .company-title__sub {
    font-weight: 400;
    font-size: 22px;
    line-height: 28px;
    margin-top: 2px;
  }

  .person-name {
    position: absolute;
    left: 55px;
    top: 292px;
    height: 53px;
    line-height: 53px;
    font-family: "Exo 2", sans-serif;
    font-weight: 300;
    font-size: 22px;
    color: var(--ink);
  }
  .web-contact {
    position: absolute;
    right: 52px;
    top: 292px;
    height: 53px;
    line-height: 53px;
    font-family: "Nunito", sans-serif;
    font-size: 22px;
    color: var(--ink);
  }

  .address, .phones {
    position: absolute;
    top: 371px;
    color: var(--white);
    font-size: 17px;
    line-height: 22px;
  }
  .address { left: 56px; }
  .phones { left: 553px; }

  .company-korean {
    position: absolute;
    right: 52px;
    top: 48px;
    font-family: "Noto Sans KR", sans-serif;
    font-weight: 400;
    font-size: 23px;
    color: var(--white);
    letter-spacing: 1px;
  }
  .person-korean {
    position: absolute;
    left: 0;
    width: 100%;
    top: 294px;
    height: 52px;
    line-height: 52px;
    text-align: center;
    font-family: "Noto Sans KR", sans-serif;
    font-weight: 400;
    font-size: 28px;
    color: var(--blue-name);
    letter-spacing: 2px;
  }
  .info-col {
    position: absolute;
    top: 374px;
    color: var(--muted);
    font-family: "Lato", "Noto Sans KR", sans-serif;
    font-size: 16.5px;
    line-height: 21px;
  }
  .info-col svg { display: block; margin-bottom: 4px; }
  .info-col--address { left: 56px; font-family: "Noto Sans KR", sans-serif; font-weight: 300; }
  .info-col--phone { left: 353px; }
  .info-col--web { left: 599px; }
</style>
</head>
<body>
<div class="canvas">

  <section class="card card--english" aria-label="English side">
    <div class="band band--black"></div>
    <div class="band band--white"></div>
    <div class="band band--navy"></div>

    <div class="brand">
      <div class="brand__square"></div>
      <div class="brand__name">CORWELL<br>INSIGHT<br>PARTNERS</div>
    </div>

    <div class="company-title">
      <div class="company-title__main">CORWELL</div>
      <div class="company-title__sub">INSIGHT PARTNERS, INC.</div>
    </div>

    <div class="person-name">DANIEL PARK</div>
    <div class="web-contact">daniel@corwellip.com | www.corwellip.com</div>

    <div class="address">
      #507, HANBIT BLDG,<br>
      82 MAEBONGSAN-RO,<br>
      DOBONG-GU, SEOUL, 01327, KOREA
    </div>
    <div class="phones">
      Tel. +82 2 718 4052<br>
      Fax. +82 2 864 1097<br>
      Mobile. +82 10 7264 8815
    </div>
  </section>

  <section class="card card--korean" aria-label="Korean side" lang="ko">
    <div class="band band--black"></div>
    <div class="band band--white"></div>
    <div class="band band--navy"></div>

    <div class="brand">
      <div class="brand__square"></div>
      <div class="brand__name">CORWELL<br>INSIGHT<br>PARTNERS</div>
    </div>

    <div class="company-korean">회사명: 코웰인사이트파트너스(주)</div>
    <div class="person-korean">박도현</div>

    <div class="info-col info-col--address">
      <svg width="22" height="18" viewBox="0 0 22 18" aria-hidden="true">
        <path d="M11 1 L1 9 H4 V17 H9 V12 H13 V17 H18 V9 H21 Z" fill="#ffffff"/>
      </svg>
      서울시 도봉구 매봉산로 82<br>
      한빛빌딩 507호
    </div>

    <div class="info-col info-col--phone">
      <svg width="22" height="18" viewBox="0 0 22 18" aria-hidden="true">
        <path d="M2 6 C2 2 20 2 20 6 V8 H15 V6 H7 V8 H2 Z" fill="#ffffff"/>
        <path d="M5 9 H17 L19 17 H3 Z" fill="#ffffff"/>
        <circle cx="11" cy="13" r="2.2" fill="#1b2251"/>
      </svg>
      Mobile. 010 7264 8815<br>
      Tel. 02 718 4052<br>
      Fax. 02 864 1097
    </div>

    <div class="info-col info-col--web">
      <svg width="22" height="18" viewBox="0 0 22 18" aria-hidden="true">
        <rect x="2" y="1.5" width="18" height="11" fill="none" stroke="#ffffff" stroke-width="2"/>
        <rect x="9" y="13" width="4" height="2.5" fill="#ffffff"/>
        <rect x="6" y="15.5" width="10" height="2" fill="#ffffff"/>
      </svg>
      daniel@corwellip.com<br>
      www.corwellip.com
    </div>
  </section>

</div>
</body>
</html>
```